Need a website where people can find information about the newly formed Northmere Property Review Board. Soon after, we will need a place to publish our findings as we audit each municipality in the State of Wisconsin. I have a logo (designed by Pixel Harbor), a MS Word document showing the content and a set of images to choose from that we can purchase from Snapvine.com (found here https://www.snapvinephoto.example/teamwork/lists/-Qb7TrWmXa2NoPLzdRy-Hk)

```html
<!DOCTYPE html>
<html lang="en">
<head>
<meta charset="utf-8">
<title>Audit Methods – Northmere Property Review Board</title>
<link href="https://fonts.googleapis.com/css2?family=Roboto:wght@300;400;500;700&family=Work+Sans:wght@700&display=swap" rel="stylesheet">
<style>
  :root {
    --green: #3d8712;
    --ink: #111111;
    --text: #555555;
    --white: #ffffff;
    --footer: #111111;
    --rule: #4a4a4a;
  }
  * { margin: 0; padding: 0; box-sizing: border-box; }
  html, body { width: 1105px; height: 1200px; overflow: hidden; background: var(--white); }
  body { position: relative; font-family: "Roboto", sans-serif; }

  .hero { position: absolute; top: 0; left: 0; width: 1105px; height: 470px; }
  .hero svg { display: block; }

  .brand {
    position: absolute; top: 22px; left: 103px;
    display: flex; align-items: center; gap: 10px;
  }
  .brand-mark { width: 18px; height: 18px; background: var(--green); flex: none; }
  .brand-name {
    width: 140px; color: var(--white); font-weight: 700; font-size: 14px;
    line-height: 17px; text-transform: uppercase;
  }

  .main-nav {
    position: absolute; top: 50px; right: 103px;
    display: flex; gap: 28px;
  }
  .main-nav a {
    color: var(--white); text-decoration: none; font-weight: 700;
    font-size: 13.5px; text-transform: uppercase; letter-spacing: 0.1px;
    text-shadow: 0 1px 3px rgba(0,0,0,.35);
  }

  .methods {
    position: absolute; top: 506px; left: 103px; width: 899px; text-align: center;
  }
  .methods h1 {
    font-family: "Work Sans", sans-serif; font-weight: 700; font-size: 32px;
    color: var(--ink); letter-spacing: 0.5px; margin-bottom: 24px;
  }
  .methods p {
    font-weight: 300; font-size: 14.2px; line-height: 23.7px;
    color: var(--text); margin-bottom: 18px;
  }

  .site-footer { position: absolute; left: 0; top: 956px; width: 1105px; height: 244px; }
  .site-footer svg { position: absolute; top: 0; left: 0; }
  .footer-brand {
    position: absolute; top: 78px; left: 0; width: 1105px; text-align: center;
    color: var(--white); font-weight: 700; font-size: 15px; text-transform: uppercase;
    line-height: 20px;
  }
  .footer-rule {
    position: absolute; top: 188px; left: 103px; width: 899px;
    border-top: 1px solid var(--rule);
  }
  .copyright {
    position: absolute; top: 204px; left: 0; width: 1105px; text-align: center;
    color: var(--white); font-size: 13px;
  }
  .legal {
    position: absolute; top: 204px; right: 103px; color: var(--white); font-size: 13px;
  }
  .legal a { color: var(--white); text-decoration: none; }
  .legal span { margin: 0 10px; }
</style>
</head>
<body>
  <header class="hero">
    <svg width="1105" height="470" viewBox="0 0 1105 470">
      <defs>
        <radialGradient id="gears" cx="50%" cy="55%" r="70%">
          <stop offset="0" stop-color="#8f8f8f"/>
          <stop offset="0.5" stop-color="#6b6b6b"/>
          <stop offset="1" stop-color="#2e2e2e"/>
        </radialGradient>
        <filter id="lift" x="-50%" y="-50%" width="200%" height="200%">
          <feDropShadow dx="0" dy="3" stdDeviation="4" flood-opacity="0.25"/>
        </filter>
      </defs>
      <path class="hero-band" d="M0 284 Q552 596 1105 284 L1105 296 Q552 604 0 296 Z" fill="var(--green)"/>
      <path d="M0 0 H1105 V284 Q552 560 0 284 Z" fill="url(#gears)" role="img" aria-label="Close-up photograph of metal gears engraved with the words audit, analysis, report and data"/>
      <circle cx="552" cy="416" r="53" fill="none" stroke="var(--white)" stroke-width="1.5"/>
      <circle cx="552" cy="416" r="30" fill="var(--white)" filter="url(#lift)"/>
      <path d="M552 405 V424 M544 416 L552 425 L560 416" fill="none" stroke="var(--green)" stroke-width="4.5" stroke-linecap="round" stroke-linejoin="round"/>
    </svg>
    <div class="brand">
      <span class="brand-mark"></span>
      <span class="brand-name">Northmere Property Review Board</span>
    </div>
    <nav class="main-nav">
      <a href="#">Home</a>
      <a href="#">Audit Results</a>
      <a href="#">Recommendations</a>
      <a href="#">Blog</a>
      <a href="#">Contact Us</a>
    </nav>
  </header>

  <main class="methods">
    <h1>AUDIT METHODS</h1>
    <p>We audit each municipalities’ electronic property tax assessment records. Municipalities are required to keep their assessment records in electronic form, but some do not because the Department of Revenue, who made up the requirement, doesn’t enforce their own administrative rules. Not understanding what the word “requirement” means is a longstanding problem at the Department of Revenue and one of the many causes of non-uniformity.</p>
    <p>Problem with uniformity can nearly always be tracked back to problem with assessed values. Most real estate in Wisconsin is supposed to be assessed at 100% of market value. The largest exceptions are agricultural land, land in DNR forest programs and exempt property.</p>
    <p>Each municipality should be using CAMA software to calculate property values. For those that do, we use reports generated by their CAMA software to prove or disprove that assessed values are uniform. We also look for evidence that property assessed at less than full market value meets the requirements.</p>
    <p>Any municipality not using CAMA software automatically fails our test. In addition, if the CAMA software used does not support all three recognized approaches to value (cost, sales comparison and income), it also fails our test.</p>
  </main>

  <footer class="site-footer">
    <svg width="1105" height="244" viewBox="0 0 1105 244">
      <path d="M0 141 Q552 -141 1105 141 V244 H0 Z" fill="var(--green)"/>
      <path d="M0 146 Q552 -118 1105 146 V244 H0 Z" fill="var(--footer)"/>
    </svg>
    <div class="footer-brand">Northmere Property<br>Review Board</div>
    <div class="footer-rule"></div>
    <p class="copyright">© 2022 NPRB &nbsp;|&nbsp; All Rights Reserved</p>
    <p class="legal"><a href="#">Privacy Policy</a><span>|</span><a href="#">Terms &amp; Conditions</a></p>
  </footer>
</body>
</html>
```